Oral Surgery Office Referral Forms and Stationary Designs

I want something like the ones you made for Harbor Crest Oral Surgery. Please use my logo for color scheme and refer to this URL:

https://www.plornexa.example/design/552031

I would also like similar business cards with appointment date/time as well as stationaries.

Target Market(s)

Referring dentists

Industry/Entity Type

Office

Font styles to use
Serif

Requirements
Must have
• same as harbor crest oral surgery forms, I will add or delete items as I find fit once the design is ready

```html
<!DOCTYPE html>
<html lang="en">
<head>
<meta charset="utf-8">
<title>Halvern Oral Surgery – Stationery Set</title>
<link rel="stylesheet" href="https://fonts.googleapis.com/css2?family=Roboto:wght@300;400;500;700&display=swap">
<style>
:root{
  --bg:#e3e3e3;
  --paper:#f7f7f7;
  --white:#ffffff;
  --charcoal:#3f3f40;
  --green:#27e07a;
  --green-text:#3cc46e;
  --ink:#333333;
  --line:#bfe9cf;
}
*{box-sizing:border-box;margin:0;padding:0}
html,body{width:1200px;height:496px;overflow:hidden;background:var(--bg);font-family:"Roboto",sans-serif;color:var(--ink)}
.canvas{position:relative;width:1200px;height:496px}
.sheet{position:absolute;background:var(--paper);box-shadow:0 1px 3px rgba(0,0,0,.25);overflow:hidden}
.abs{position:absolute}

/* header band: flat charcoal block with a single green rule */
.band{position:absolute;left:0;top:0;width:100%;background:var(--charcoal);border-bottom:2.5px solid var(--green)}

/* brand name: single line, one weight, one colour, one square beside it */
.brand{position:absolute;display:flex;align-items:center;gap:5px;font-weight:400;color:var(--charcoal);white-space:nowrap;line-height:1}
.brand .mark{display:inline-block;background:var(--green)}
.brand.light{color:var(--white)}

/* letterhead */
.letterhead{left:34px;top:36px;width:298px;height:420px}
.letterhead .band{height:54px}
.letterhead .contact{left:27px;top:10px;color:var(--white);font-size:4.3px;line-height:1.45}
.letterhead .contact b{font-weight:500}
.letterhead .contact i{display:inline-block;width:3px;height:3px;border-radius:50%;background:var(--green);margin-right:3px;vertical-align:middle}
.letter-body{left:27px;top:118px;width:248px;font-size:4.1px;line-height:1.55;color:#555}
.letter-body .salute{font-size:7px;color:var(--ink);margin-bottom:12px;font-weight:300}
.letter-body p{margin-bottom:6px}
.letter-body .close{margin-top:12px}
.signature{left:27px;top:292px;width:56px;height:24px;background:linear-gradient(90deg,#dfe7f3,#eef2f8);border-radius:3px}

/* envelopes */
.env-back{left:346px;top:167px;width:300px;height:137px}
.env-back .flap{position:absolute;left:0;top:0;display:block}
.env-front{left:346px;top:320px;width:300px;height:136px}
.env-front .band{height:42px}
.env-return{left:16px;top:109px;font-size:4.3px;line-height:1.4;color:#555}
.env-return b{font-weight:500;color:var(--ink)}

/* referral form */
.form-front{left:661px;top:42px;width:241px;height:416px;background:var(--white)}
.form-front .band{height:50px}
.form-back{left:914px;top:42px;width:244px;height:416px;background:var(--white)}
.form-head{left:11px;top:9px;font-size:5px;line-height:1.35;color:var(--white);font-weight:500}
.form-head .title{color:var(--green);font-size:5.6px}
.field{position:absolute;left:11px;width:220px;border-bottom:1.4px solid var(--line);font-size:5.6px;height:11px;color:var(--ink)}
.field .ph{position:absolute;color:#a9a9a9;font-size:5.4px}
.days{left:150px;top:81px;display:grid;grid-template-columns:32px 30px;row-gap:2px;font-size:4.6px}
.cb{display:inline-block;width:4.5px;height:4.5px;border:.6px solid #7fd9a2;margin-right:3px;vertical-align:-0.5px;background:var(--white)}
.online{left:11px;top:202px;width:210px;font-size:5.4px;line-height:1.6}
.chart{position:absolute;border-radius:2px}

/* back */
.sec{position:absolute;font-size:5.6px;font-weight:500}
.opt{position:absolute;font-size:5.2px;white-space:nowrap}
.opt-line{position:absolute;height:1px;background:var(--green)}
.instructions{left:10px;top:192px;width:224px;height:152px;border:1.4px solid #a8e8bf;padding:4px 5px;font-size:3.9px;line-height:1.5;color:var(--green-text)}
.instructions h4{font-size:4.6px;font-weight:500;color:var(--ink);margin-bottom:1px}
.map{left:11px;top:356px;width:84px;height:44px;background:linear-gradient(135deg,#cfcfcf,#9c9c9c);border:1.4px solid #444}
.back-contact{left:100px;top:357px;font-size:4.8px;line-height:2.1;font-weight:500}
</style>
</head>
<body>
<main class="canvas">

  <!-- Letterhead -->
  <section class="sheet letterhead" aria-label="Letterhead">
    <div class="band"></div>
    <div class="abs contact">
      <b>Halvern Oral Surgery</b><br>4210 Cedarview Lane<br>Millbrook, Oregon 97481<br>
      <i></i>(555) 014.2290<br><i></i>info@halvernsurgery.example<br><i></i>www.halvernsurgery.example
    </div>
    <div class="brand light" style="right:18px;top:22px;font-size:10px">
      <span class="mark" style="width:7px;height:7px"></span>Halvern Oral Surgery
    </div>
    <div class="abs letter-body">
      <div class="salute">Dear Mr. Porter,</div>
      <p>Thank you for referring your patient to our practice. We have reviewed the records and x-rays you sent and have scheduled a consultation to discuss the planned treatment, the anesthesia options and the expected recovery time with the patient and family.</p>
      <p>During the visit we will take any further images that are needed, confirm the medical history and answer questions. A written treatment plan will follow by mail so you can keep it with the chart for future care and check-ups.</p>
      <p>After surgery the patient will be seen for a follow-up visit within two weeks. Once healing is complete we will return the patient to your office with a summary of the procedure and any notes for the restorative phase of care.</p>
      <p>We value working with you and look forward to helping more of your patients. Please call our office if you have any questions or need to send updated records.</p>
      <div class="close">Sincerely,</div>
    </div>
    <div class="abs signature" role="img" aria-label="Handwritten signature of Owen Porter"></div>
  </section>

  <!-- Envelope back -->
  <section class="sheet env-back" aria-label="Envelope back">
    <svg class="flap" width="300" height="44" viewBox="0 0 300 44">
      <path d="M0 0H300V4L282 36Q278 43 268 43H32Q22 43 18 36L0 4Z" fill="var(--charcoal)"/>
    </svg>
    <div class="brand light" style="left:106px;top:20px;font-size:8px">
      <span class="mark" style="width:6px;height:6px"></span>Halvern Oral Surgery
    </div>
  </section>

  <!-- Envelope front -->
  <section class="sheet env-front" aria-label="Envelope front">
    <div class="band"></div>
    <div class="brand light" style="left:18px;top:17px;font-size:9px">
      <span class="mark" style="width:6px;height:6px"></span>Halvern Oral Surgery
    </div>
    <div class="abs env-return"><b>Halvern Oral Surgery</b><br>4210 Cedarview Lane<br>Millbrook, Oregon 97481</div>
  </section>

  <!-- Referral form front -->
  <section class="sheet form-front" aria-label="Referral form front">
    <div class="band"></div>
    <div class="abs form-head">
      <div class="title">HALVERN ORAL SURGERY</div>
      <div style="margin-top:3px">4210 Cedarview Lane, Millbrook, Oregon 97481</div>
      <div>P (555) 014.2290 &nbsp;F (555) 014.2291</div>
      <div>www.halvernsurgery.example</div>
    </div>

    <div class="field" style="top:62px">Today's Date<span class="ph" style="left:56px">DD &nbsp;/&nbsp; MM &nbsp;/&nbsp; YYYY</span></div>
    <div class="field" style="top:80px;width:138px">Appt. date<span class="ph" style="left:56px">DD &nbsp;/&nbsp; MM &nbsp;/&nbsp; YYYY</span><span style="position:absolute;left:126px">Day</span></div>
    <div class="field" style="top:98px;width:138px">Time<span class="ph" style="left:98px;color:var(--ink)">AM/PM</span></div>
    <div class="abs days">
      <span><i class="cb"></i>Mon</span><span><i class="cb"></i>Tues</span>
      <span><i class="cb"></i>Wed</span><span><i class="cb"></i>Thurs</span>
      <span><i class="cb"></i>Fri</span><span><i class="cb"></i>Sat</span>
      <span><i class="cb"></i>Sun</span>
    </div>
    <div class="field" style="top:116px">Patient's Name</div>
    <div class="field" style="top:134px">Patient's Phone Number</div>
    <div class="field" style="top:152px">Referred by</div>
    <div class="field" style="top:170px;border-bottom:none">Additional Comments</div>

    <p class="abs online">You can save time by going online. Register and update your health history today at www.halvernsurgery.example</p>

    <div class="chart" style="left:11px;top:234px;width:148px;height:76px;background:linear-gradient(#eef3fa,#dbe5f2);border:1.4px solid #8fb0d6" role="img" aria-label="Numbered permanent teeth chart, 1 to 32, right and left"></div>
    <div class="chart" style="left:167px;top:230px;width:68px;height:84px;background:radial-gradient(circle,#ffffff 30%,#e3e6ea 75%)" role="img" aria-label="Deciduous teeth arch diagram"></div>
    <div class="chart" style="left:15px;top:322px;width:188px;height:80px;background:linear-gradient(90deg,#ececec,#f6f6f6,#ececec)" role="img" aria-label="Soft tissue chart showing two open mouth diagrams"></div>
  </section>

  <!-- Referral form back -->
  <section class="sheet form-back" aria-label="Referral form back">
    <div class="sec" style="left:26px;top:17px">PROCEDURE</div>
    <div class="opt" style="left:26px;top:28px"><i class="cb"></i>Extraction</div>
    <div class="opt" style="left:70px;top:28px"><i class="cb"></i>Implants</div>
    <div class="opt" style="left:110px;top:28px"><i class="cb"></i>Consultation</div>
    <div class="opt" style="left:162px;top:28px"><i class="cb"></i>Radiographs</div>

    <div class="opt" style="left:18px;top:45px"><i class="cb"></i>Wistom Teeth</div>
    <div class="opt" style="left:18px;top:55px"><i class="cb"></i>Extraction</div>
    <div class="opt" style="left:18px;top:65px"><i class="cb"></i>Implants</div>
    <div class="opt" style="left:18px;top:75px"><i class="cb"></i>Bone Grafting</div>
    <div class="opt" style="left:18px;top:85px"><i class="cb"></i>Exposure and bonding</div>
    <div class="opt" style="left:18px;top:95px"><i class="cb"></i>Biopsy(SOFT or Hard Tissue)</div>

    <div class="opt" style="left:102px;top:45px"><i class="cb"></i>Lesion Evaluation</div>
    <div class="opt" style="left:102px;top:55px"><i class="cb"></i>Infection (I&amp;D)</div>
    <div class="opt" style="left:102px;top:65px"><i class="cb"></i>Alveoloplasty</div>
    <div class="opt" style="left:102px;top:75px"><i class="cb"></i>Frenectomy</div>
    <div class="opt" style="left:102px;top:85px"><i class="cb"></i>Orthognathic</div>
    <div class="opt" style="left:102px;top:95px"><i class="cb"></i>TMJ</div>
    <div class="opt" style="left:102px;top:105px"><i class="cb"></i>Other</div>
    <div class="opt-line" style="left:110px;top:117px;width:36px"></div>

    <div class="sec" style="left:165px;top:45px;font-size:5.2px">Implants</div>
    <div class="opt" style="left:165px;top:55px"><i class="cb"></i>Norvex</div>
    <div class="opt" style="left:165px;top:65px"><i class="cb"></i>Strelan</div>
    <div class="opt" style="left:165px;top:75px"><i class="cb"></i>Astrio</div>
    <div class="opt" style="left:165px;top:85px"><i class="cb"></i>Vantis</div>
    <div class="opt" style="left:165px;top:95px"><i class="cb"></i>Other</div>
    <div class="opt-line" style="left:170px;top:106px;width:38px"></div>

    <div class="sec" style="left:18px;top:124px">Surgical Template</div>
    <div class="opt" style="left:10px;top:134px"><i class="cb"></i>To be provided by Restorative dentist</div>
    <div class="opt" style="left:146px;top:134px"><i class="cb"></i>To be fabricated by the surgeon</div>
    <div class="opt" style="left:10px;top:144px"><i class="cb"></i>Other</div>
    <div class="opt-line" style="left:40px;top:150px;width:62px"></div>

    <div class="sec" style="left:18px;top:159px">Radiographs</div>
    <div class="opt" style="left:10px;top:168px"><i class="cb"></i>Being Mailed/emailed</div>
    <div class="opt" style="left:91px;top:168px"><i class="cb"></i>Given to the Patient</div>
    <div class="opt" style="left:156px;top:168px"><i class="cb"></i>Please Take</div>
    <div class="opt" style="left:10px;top:177px"><i class="cb"></i>Other</div>
    <div class="opt-line" style="left:40px;top:183px;width:82px"></div>

    <div class="abs instructions">
      <h4>Patient Instructions</h4>
      <p>PLEASE NOTE THAT IN MOST INSTANCES THE PATIENT IS FIRST SEEN FOR CONSULTATION TO REVIEW THE HEALTH HISTORY, DECIDE ON THE MOST APPROPRIATE ANESTHESIA AND TREATMENT PLAN, AND SCHEDULE THE SURGERY AT A SEPARATE APPOINTMENT.</p>
      <p>Please assist us by having the following information available with you at the time of appointment: Your surgical referral slip and any x-rays if applicable, a list of medications, insurance policy information.</p>
      <p>IMPORTANT: All patients unmarried or under the age of 19 must be accompanied by a parent or guardian during the consultation and treatment visits.</p>
      <p style="margin-top:3px">SPECIAL INSTRUCTIONS FOR PATIENTS HAVING I.V. SEDATION / GENERAL ANESTHESIA:</p>
      <p>&nbsp;- NO FOOD OR DRINK (including WATER) AT LEAST 8 HOURS PRIOR TO YOUR SURGERY UNLESS OTHERWISE INDICATED BY THE SURGEON. Some medications may be continued and this will be discussed at your consultation.</p>
      <p>&nbsp;- A responsible adult must accompany you and REMAIN in the office during the entire treatment. They must also be able to drive you home. YOU cannot drive until the next day.</p>
      <p>&nbsp;- Eat a light and easily digestible meal the night before the procedure. Do not drink alcoholic beverages the night before.</p>
      <p>&nbsp;- Wear comfortable clothing with sleeves which are easy to push up.</p>
    </div>

    <div class="abs map" role="img" aria-label="Location map of the office"></div>
    <div class="abs back-contact">
      4210 Cedarview Lane, Millbrook, Oregon 97481<br>P (555) 014.2290<br>F (555) 014.2291<br>www.halvernsurgery.example
    </div>
    <div class="brand" style="left:152px;top:378px;font-size:7.5px">
      <span class="mark" style="width:5px;height:5px"></span>Halvern Oral Surgery
    </div>
  </section>

</main>
</body>
</html>
```